PDBA website design

We need a page template website design for a cms website. Please see the brief attached for the details.
The client is the Pacific Downhorn Breeders Association which is an organisation promoting the White Suffolk Sheep Breed within Australia.

Reason: So that my top few designs can make changes and re-submit.

Target Market(s)

See attached brief

```html
<!DOCTYPE html>
<html lang="en">
<head>
<meta charset="utf-8">
<title>PDBA – Pacific Downhorn Breeders Association</title>
<link rel="stylesheet" href="https://fonts.googleapis.com/css2?family=Open+Sans:ital,wght@0,400;0,600;0,700;1,700&family=Noto+Sans:wght@400;600&display=swap">
<style>
:root{
  --green:#0e9444;
  --lime:#c7cf18;
  --yellow:#ecea12;
  --ink:#2b2b2b;
  --panel:#f3f3f3;
  --line:#dcdcdc;
  --band:#e9e9e9;
  --footer:#2a2a2a;
  --footer-text:#c9c9c9;
  --date-red:#a0111c;
}
*{box-sizing:border-box;margin:0;padding:0}
html,body{width:889px;height:1200px;overflow:hidden}
body{position:relative;background:#fff;font-family:"Open Sans",Arial,sans-serif;color:var(--ink)}
.abs{position:absolute}
a{color:inherit;text-decoration:none}

.site-header{left:0;top:0;width:889px;height:98px;background:linear-gradient(#f4f4f4,#e9e9e9);border-top:2px solid var(--lime)}
.brand{left:74px;top:14px;display:flex;align-items:center;gap:8px}
.brand-mark{width:52px;height:52px;background:var(--green);border-radius:50%}
.brand-name{font-size:30px;font-weight:700;color:var(--green);line-height:1}
.brand-tag{left:140px;top:67px;font-size:10px;color:var(--green);white-space:nowrap}
.account-tabs{left:645px;top:0;display:flex;gap:3px}
.account-tabs a{display:block;width:80px;height:27px;background:var(--lime);color:#fff;font-size:9px;font-weight:700;text-align:center;line-height:27px;border-radius:0 0 3px 3px}
.phone{left:650px;top:48px;display:flex;align-items:center;gap:8px;font-size:16px;color:#333;white-space:nowrap}
.phone svg{width:26px;height:26px}

.main-nav{left:74px;top:106px;width:741px;height:32px;background:var(--green);display:flex;align-items:center;justify-content:space-between;padding:0 32px 0 21px;box-shadow:0 6px 8px -4px rgba(0,0,0,.35)}
.main-nav a{color:#fff;font-size:11px;font-weight:600;white-space:nowrap}

.hero{left:74px;top:160px;width:741px;height:281px;background:linear-gradient(#b9d4ea 0%,#d9e6ee 22%,#4d6a3d 30%,#3d5a2c 50%,#a7a27f 62%,#5e9a3b 80%,#4f8a2e 100%);border-bottom:3px solid var(--lime)}

.tab{top:487px;height:31px;padding:0 7px;font-family:"Noto Sans",Arial,sans-serif;font-size:13px;font-weight:600;line-height:31px;border-radius:3px 3px 0 0;white-space:nowrap;color:#fff}
.tab-active{left:73px;width:166px;background:var(--green)}
.tab-idle{left:242px;width:224px;background:linear-gradient(#d8d8d8,#b5b5b5);padding-left:10px}
.feature-panel{left:73px;top:518px;width:501px;height:166px;background:var(--panel);border:1px solid var(--line);border-radius:0 4px 4px 4px}
.feature-photo{left:82px;top:530px;width:171px;height:115px;background:linear-gradient(#9fb3c8 0%,#7c7f6a 45%,#c8b9a0 70%,#a5562c 100%);border:3px solid #fff;box-shadow:0 0 2px rgba(0,0,0,.3)}
.pg-badge{left:270px;top:530px;width:27px;height:24px;background:var(--green);color:#fff;font-size:10px;font-weight:700;text-align:center;line-height:24px;border-radius:3px}
.feature-title{left:305px;top:531px;font-size:12px;color:#333;white-space:nowrap}
.feature-date{left:305px;top:546px;font-size:8px;color:var(--date-red)}
.feature-copy{left:268px;top:566px;width:290px;font-family:Arial,sans-serif;font-size:9px;line-height:14.8px;color:#333}

.news-head{left:602px;top:489px;width:192px;height:25px;background:var(--green);color:#fff;font-family:"Noto Sans",Arial,sans-serif;font-size:13px;font-weight:600;padding-left:7px;line-height:25px;border-radius:3px}
.event{left:605px;width:190px;height:45px}
.event-thumb{position:absolute;left:0;top:1px;width:32px;height:28px;background:linear-gradient(#e6e6e6,#9a9a9a);border:2px solid #fff;box-shadow:0 0 2px rgba(0,0,0,.4)}
.event-text{position:absolute;left:42px;top:0;width:140px;font-family:Arial,sans-serif;font-size:9px;line-height:10.5px;color:#333}
.event-text span{color:var(--green)}
.event-date{position:absolute;right:14px;top:33px;font-family:Arial,sans-serif;font-size:8px;font-weight:700;color:var(--green)}

.latest-band{left:0;top:718px;width:889px;height:216px;background:var(--green)}
.latest-title{left:78px;top:727px;font-family:"Noto Sans",Arial,sans-serif;font-size:17px;font-weight:600;color:#fff}
.latest-item{left:79px;width:487px;height:50px;border-bottom:1px dotted #6cc08c}
.latest-thumb{position:absolute;left:0;top:0;width:50px;height:44px;border:2px solid #fff}
.latest-head{position:absolute;left:62px;top:0;font-size:9px;font-style:italic;font-weight:700;color:var(--yellow);white-space:nowrap}
.latest-copy{position:absolute;left:62px;top:13px;width:430px;font-size:8.5px;line-height:12px;color:#eaf5ec}
.video{left:606px;top:748px;width:193px;height:156px;background:#111;border:1px solid #000}
.video-frame{left:611px;top:752px;width:183px;height:128px;background:linear-gradient(#8a9a88,#6f7d55 55%,#58683a)}
.video-bar{left:606px;top:885px;width:193px;height:19px;background:#e8e8e8;font-size:5px;color:#555;padding:10px 4px 0;display:flex;justify-content:space-between}
.play{left:680px;top:797px}

.partners{left:0;top:934px;width:889px;height:92px;background:var(--band)}
.partner{top:963px;height:34px;background:#cfcfcf;border-radius:4px}

.site-footer{left:0;top:1026px;width:889px;height:174px;background:var(--footer)}
.foot-col{top:1052px}
.foot-col h3{font-family:"Noto Sans",Arial,sans-serif;font-weight:400;font-size:15px;color:#fff;margin-bottom:8px;white-space:nowrap}
.foot-col li{list-style:none;font-size:10px;color:var(--footer-text);line-height:18.6px;white-space:nowrap}
.social{display:flex;gap:3px}
.social span{width:20px;height:20px;border-radius:50%;background:#fff;display:block}
.payments{display:flex;gap:3px}
.payments span{background:#fff;color:#1d3d8f;font-size:8px;font-weight:700;padding:4px 4px;border-radius:2px}
.copyright{right:81px;top:1124px;font-size:9px;color:var(--footer-text);text-align:right;line-height:18.6px;white-space:nowrap}
</style>
</head>
<body>

<header class="abs site-header">
  <div class="abs brand"><span class="brand-mark"></span><span class="brand-name">PDBA</span></div>
  <div class="abs brand-tag">Stronger Every Season</div>
  <nav class="abs account-tabs"><a href="#">LOGIN</a><a href="#">REGISTER</a></nav>
  <div class="abs phone">
    <svg viewBox="0 0 26 26"><circle cx="13" cy="13" r="12" fill="none" stroke="#333" stroke-width="1.5"/><path d="M9 7c-2 2-1 6 2 9s7 4 9 2l-2-3-2 1c-1 0-4-3-4-4l1-2z" fill="none" stroke="#333" stroke-width="1.3"/></svg>
    +(100) 555 0142
  </div>
</header>

<nav class="abs main-nav">
  <a href="#">HOME</a><a href="#">ABOUT US</a><a href="#">CAREERS</a><a href="#">LOCATIONS</a><a href="#">SERVICES</a><a href="#">TECHNOLOGY</a><a href="#">CONTACT US</a>
</nav>

<div class="abs hero" role="img" aria-label="Flock of white sheep grazing on green pasture below forested hills"></div>

<div class="abs tab tab-active">Featured Auction Fader</div>
<div class="abs tab tab-idle">Featured Asset for Sale Fader</div>
<div class="abs feature-panel"></div>
<div class="abs feature-photo" role="img" aria-label="Line of sheep on red earth in front of a hill"></div>
<div class="abs pg-badge">PG</div>
<div class="abs feature-title">Featured Auction Fader</div>
<div class="abs feature-date">May 15, 2012</div>
<p class="abs feature-copy">Lorem Ipsum is simply dummy text of the printing and typesetting industry. Lorem Ipsum has been the industry's standard dummy text ever since the 1500s, when an unknown printer took a galley of type and scrambled it to make a type specimen book. It has survived not only five centuries, but also the leap into electronic typesetting, remaining essentially unchanged&nbsp; but also the leap</p>

<div class="abs news-head">News/Events</div>
<div class="abs event" style="top:528px"><div class="event-thumb" role="img" aria-label="Member portrait"></div><p class="event-text">Lorem Ipsum is simply text of the also&nbsp; a subject a <span>subject matter printing</span></p><div class="event-date">May 15 , 2012</div></div>
<div class="abs event" style="top:579px"><div class="event-thumb" role="img" aria-label="Member portrait"></div><p class="event-text">Lorem Ipsum is simply text of the also&nbsp; a subject a <span>subject matter printing</span></p><div class="event-date">May 15 , 2012</div></div>
<div class="abs event" style="top:629px"><div class="event-thumb" role="img" aria-label="Member portrait"></div><p class="event-text">Lorem Ipsum is simply text of the also&nbsp; a subject a <span>subject matter printing</span></p><div class="event-date">May 15 , 2012</div></div>

<section class="abs latest-band"></section>
<h2 class="abs latest-title">Latest News</h2>
<div class="abs latest-item" style="top:761px"><div class="latest-thumb" role="img" aria-label="Green crop leaves" style="background:linear-gradient(#3f8f2a,#8bc34a)"></div><div class="latest-head">Quisque tincidunt accumsan dolor, sed vestibulum est.</div><p class="latest-copy">Pellentesque sed faucibus sem. Pellentesque feugiat ultricies molestie. Nunc imperdiet mi accumsan turpis ornare ut rutrum massa dictum. Phasellus tempus, massa a vestibulum egestas, urna orci pulvinar lectus...</p></div>
<div class="abs latest-item" style="top:812px"><div class="latest-thumb" role="img" aria-label="Sunflower field at sunset" style="background:linear-gradient(#7a5a6a,#e09a3a 55%,#3e6a22)"></div><div class="latest-head">Quisque tincidunt accumsan dolor, sed vestibulum est.</div><p class="latest-copy">Pellentesque sed faucibus sem. Pellentesque feugiat ultricies molestie. Nunc imperdiet mi accumsan turpis ornare ut rutrum massa dictum. Phasellus tempus, massa a vestibulum egestas, urna orci pulvinar lectus...</p></div>
<div class="abs latest-item" style="top:863px;border-bottom:none"><div class="latest-thumb" role="img" aria-label="Green crop leaves" style="background:linear-gradient(#3f8f2a,#8bc34a)"></div><div class="latest-head">Quisque tincidunt accumsan dolor, sed vestibulum est.</div><p class="latest-copy">Pellentesque sed faucibus sem. Pellentesque feugiat ultricies molestie. Nunc imperdiet mi accumsan turpis ornare ut rutrum massa dictum. Phasellus tempus, massa a vestibulum egestas, urna orci pulvinar lectus...</p></div>

<div class="abs video"></div>
<div class="abs video-frame" role="img" aria-label="Video still of cattle grazing in a paddock"></div>
<svg class="abs play" width="46" height="46" viewBox="0 0 46 46"><circle cx="23" cy="23" r="21" fill="rgba(255,255,255,.15)" stroke="#fff" stroke-width="2.5"/><path d="M18 14l14 9-14 9z" fill="#fff"/></svg>
<div class="abs video-bar"><span>PAUSE</span><span>share</span><span>link</span><span>MENU</span></div>

<section class="abs partners"></section>
<svg class="abs" style="left:84px;top:967px" width="20" height="30" viewBox="0 0 20 30"><path d="M16 2L4 15l12 13" fill="none" stroke="#555" stroke-width="5"/></svg>
<svg class="abs" style="left:777px;top:967px" width="20" height="30" viewBox="0 0 20 30"><path d="M4 2l12 13L4 28" fill="none" stroke="#555" stroke-width="5"/></svg>
<div class="abs partner" style="left:130px;width:46px"></div>
<div class="abs partner" style="left:222px;width:34px"></div>
<div class="abs partner" style="left:301px;width:34px;top:957px;height:44px"></div>
<div class="abs partner" style="left:372px;width:68px;top:972px;height:16px"></div>
<div class="abs partner" style="left:478px;width:48px;border-radius:50%"></div>
<div class="abs partner" style="left:557px;width:62px"></div>
<div class="abs partner" style="left:660px;width:90px"></div>

<footer class="abs site-footer"></footer>
<div class="abs foot-col" style="left:92px"><h3>Information</h3><ul><li>Main</li><li>About Us</li><li>Product List</li><li>Why Choose Us</li></ul></div>
<div class="abs foot-col" style="left:227px"><h3>Latest Products</h3><ul><li>Mauris vel lacus</li><li>Citae felis</li><li>Vestibulum volutpat</li><li>Etiam est nunc</li></ul></div>
<div class="abs foot-col" style="left:382px"><h3>Support</h3><ul><li>Order Now</li><li>Free Shipping</li><li>Customer Support</li><li>Contact Us</li></ul></div>
<div class="abs foot-col" style="left:516px"><h3>Find us on</h3><div class="social"><span></span><span></span><span></span><span></span></div></div>
<div class="abs foot-col" style="left:656px"><h3>Payment Method</h3><div class="payments"><span>Vantra</span><span>Corvell</span><span>Amplex</span><span>Paynest</span></div></div>
<div class="abs copyright">© 2013 Company Name. All right reserved.<br>Term of Use &nbsp;| Policy Privacy</div>

</body>
</html>
```